Super elegant, crisp & clean Business card design required

We recently upgraded our branding - which is on our website - tavolenstudio.com

I would like a simple, yet elegant, clean business card design please.

The font of my logo is Cinzel - and because of the natural colour - it's best to have this on a black background.

I would like to have the back of the business card - with simply my logo.

PLEASE DO NOT SUBMIT A COMPLICATED / UNCLEAN DESIGN

Industry/Entity Type

Business

Contact Information for Business Card

Danvir Okelowa Photography

Font styles to use
Other font styles liked:
• Cinzel

Requirements
Must have
• A backpage with nothing but my logo
• Simple design - stands out
Should not have
• Colour that dont align with my logo
• Over complicated '/ non symmetrical design

```html
<!DOCTYPE html>
<html lang="en">
<head>
<meta charset="utf-8">
<title>Danvir Okelowa Photography — Business Card</title>
<link href="https://fonts.googleapis.com/css2?family=Cinzel:wght@400;500&display=swap" rel="stylesheet">
<style>
  :root {
    --backdrop: #e4e4e4;
    --card-black: #0b0b0b;
    --card-white: #ffffff;
    --ink-light: #f2f2f2;
    --ink-grey: #8e8e8e;
    --ink-soft: #a8a8a8;
    --rule: #d2d2d2;
  }
  * { margin: 0; padding: 0; box-sizing: border-box; }
  html, body { width: 1200px; height: 900px; overflow: hidden; }
  body {
    background: var(--backdrop);
    font-family: "Cinzel", serif;
    position: relative;
  }
  .card {
    position: absolute;
    left: 290px;
    width: 620px;
    height: 354px;
    box-shadow: 0 10px 24px rgba(0,0,0,0.18);
  }
  .card--back { top: 70px; background: var(--card-black); }
  .card--front { top: 476px; background: var(--card-white); }

  .wordmark { position: absolute; text-align: center; }
  .wordmark__name {
    font-size: 27px;
    font-weight: 400;
    letter-spacing: 1px;
    white-space: nowrap;
  }
  .wordmark__sub {
    font-size: 11px;
    letter-spacing: 9px;
    margin-top: 4px;
    padding-left: 9px;
  }
  .card--back .wordmark {
    left: 0; right: 0; top: 150px;
    color: var(--ink-light);
  }
  .card--front .wordmark {
    left: 0; width: 330px; top: 156px;
    color: var(--ink-grey);
  }
  .card--front .wordmark__name { font-size: 21px; }
  .card--front .wordmark__sub { font-size: 9px; letter-spacing: 7px; padding-left: 7px; }

  .divider {
    position: absolute;
    left: 338px; top: 48px;
    width: 1px; height: 258px;
    background: linear-gradient(to bottom, transparent, var(--rule) 20%, var(--rule) 80%, transparent);
  }
  .contact {
    position: absolute;
    left: 372px; top: 80px;
    color: var(--ink-grey);
  }
  .contact__name { font-size: 22px; letter-spacing: 1px; }
  .contact__role { font-size: 9px; letter-spacing: 2px; color: var(--ink-soft); margin: 2px 0 18px 24px; }
  .contact__list { list-style: none; }
  .contact__item {
    display: flex; align-items: center; gap: 10px;
    font-size: 10px; letter-spacing: 1px;
    margin-bottom: 7px;
    text-transform: lowercase;
  }
  .contact__item svg { width: 12px; height: 12px; flex: none; }
  .contact__address {
    font-size: 10px; letter-spacing: 1px; line-height: 1.5;
    color: var(--ink-soft);
    margin-top: 12px;
  }
</style>
</head>
<body>
  <section class="card card--back" aria-label="Card back">
    <div class="wordmark">
      <div class="wordmark__name">Danvir Okelowa Photography</div>
    </div>
  </section>

  <section class="card card--front" aria-label="Card front">
    <div class="wordmark">
      <div class="wordmark__name">Danvir Okelowa</div>
      <div class="wordmark__sub">Photography</div>
    </div>
    <div class="divider"></div>
    <div class="contact">
      <div class="contact__name">Arlen Voss</div>
      <div class="contact__role">MANAGER</div>
      <ul class="contact__list">
        <li class="contact__item">
          <svg viewBox="0 0 12 12" fill="none" stroke="#8e8e8e" stroke-width="1.2"><rect x="3" y="1" width="6" height="10" rx="1"/></svg>
          555 0148 207
        </li>
        <li class="contact__item">
          <svg viewBox="0 0 12 12" fill="none" stroke="#8e8e8e" stroke-width="1.2"><rect x="1" y="2.5" width="10" height="7"/><path d="M1 2.5l5 4 5-4"/></svg>
          hello@tavolenstudio.com
        </li>
        <li class="contact__item">
          <svg viewBox="0 0 12 12" fill="none" stroke="#8e8e8e" stroke-width="1.2"><circle cx="6" cy="6" r="4.5"/><path d="M1.5 6h9M6 1.5c2 2.5 2 6.5 0 9M6 1.5c-2 2.5-2 6.5 0 9"/></svg>
          www.tavolenstudio.com
        </li>
      </ul>
      <div class="contact__address">Marrow Lane Studios<br>Harlow Bay, Westmere 40218</div>
    </div>
  </section>
</body>
</html>
```